OpenCart Version 2.3.0.2 redesign for Retail and wholesale off road vehicles parts & accessor...

OpenCart Version 2.3.0.2 and want to upgrade to latest version if it is possible, and redesign for Retail and wholesale off road vehicles parts & accessories we are looking for a fresh new lookwe want it easy to usewe need it to be the same with 2 language Arabic/Englishwill work with both PC/mobileFixing the issues with all the current designWe have a logo we want to keep but its OK if slightly change it to work with the storeOur current website is: http://www.lunargear.com.sa

Target Market(s)

Cars parts

Industry/Entity Type

Automotive

```html
<!DOCTYPE html>
<html lang="en">
<head>
<meta charset="utf-8">
<title>Lunar Gear – Off Road Parts &amp; Accessories</title>
<link href="https://fonts.googleapis.com/css2?family=Montserrat:wght@400;600;700;800;900&family=Roboto:wght@400;500;700&display=swap" rel="stylesheet">
<style>
:root{
  --orange:#eaa215;
  --orange-dark:#d48f0a;
  --ink:#1d1d1d;
  --text:#444;
  --muted:#8a8a8a;
  --line:#e2e2e2;
  --light:#f4f4f4;
  --band:#e9e9e9;
  --red:#e2262c;
  --white:#fff;
  --brown:#6b4a2a;
}
*{box-sizing:border-box;margin:0;padding:0}
html,body{width:1200px;height:5389px;overflow:hidden}
body{position:relative;background:var(--white);font-family:'Roboto',sans-serif;color:var(--text)}
.abs{position:absolute}
.heading-font{font-family:'Montserrat',sans-serif}

/* top bar */
.topbar{top:0;left:0;width:1200px;height:57px;background:var(--light);font-size:15px;color:var(--ink)}
.topbar .login{left:104px;top:19px}
.topbar .lang{right:104px;top:19px;display:flex;gap:26px}

/* header */
.header{top:57px;left:0;width:1200px;height:158px}
.search{left:104px;top:54px;width:215px;height:46px;border:1px solid var(--line);font-size:14px;padding:13px 14px;color:var(--muted)}
.search svg{position:absolute;right:12px;top:13px}
.logo{left:450px;top:30px;width:300px;height:100px;text-align:center}
.logo .mark{width:28px;height:28px;background:var(--brown);margin:0 auto 10px}
.logo .name{font-family:'Montserrat',sans-serif;font-weight:800;font-size:38px;color:var(--brown);letter-spacing:1px}
.header-icon{top:56px;width:46px;height:46px;border:1px solid var(--line);display:flex;align-items:center;justify-content:center}

/* nav */
.nav{top:215px;left:0;width:1200px;height:75px;background:var(--orange);display:flex;justify-content:center;align-items:center;gap:36px;font-family:'Montserrat',sans-serif;font-weight:600;font-size:16px;color:var(--white)}
.nav .active{color:var(--ink)}

/* hero */
.hero{top:290px;left:0;width:1200px;height:453px;background:radial-gradient(ellipse at 50% 35%,#3b3b3b 0%,#151515 55%,#050505 100%)}
.hero h1{position:absolute;top:130px;width:100%;text-align:center;font-family:'Montserrat',sans-serif;font-weight:800;font-size:50px;color:var(--white)}
.select{top:244px;width:190px;height:48px;background:var(--white);font-size:14px;color:var(--muted);padding:15px 18px}
.select::after{content:"";position:absolute;right:18px;top:19px;width:7px;height:7px;border-right:2px solid var(--muted);border-bottom:2px solid var(--muted);transform:rotate(45deg)}
.search-btn{top:244px;left:835px;width:188px;height:48px;background:var(--orange);color:var(--white);font-family:'Montserrat',sans-serif;font-weight:700;font-size:16px;text-align:center;line-height:48px}
.hero-arrow{top:196px;width:34px;height:34px;border:1px solid #555;border-radius:50%}

/* features */
.feature{top:843px;width:300px;text-align:center}
.feature .icon{width:86px;height:86px;border-radius:50%;border:2px solid #e4e4e4;margin:0 auto 22px;display:flex;align-items:center;justify-content:center}
.feature h3{font-family:'Montserrat',sans-serif;font-weight:700;font-size:15px;color:var(--ink);margin-bottom:12px}
.feature p{font-size:15px;line-height:22px;color:var(--muted)}

/* promos */
.promo{color:var(--white);font-family:'Montserrat',sans-serif}
.promo-year{left:104px;top:1210px;width:496px;height:234px;background:linear-gradient(135deg,#3a3a3a,#1a1a1a)}
.promo-year .t1{position:absolute;left:75px;top:60px;font-weight:800;font-size:32px;color:var(--orange)}
.promo-year .t2{position:absolute;left:175px;top:110px;font-weight:800;font-size:62px;color:var(--orange)}
.promo-new{left:104px;top:1473px;width:496px;height:236px;background:linear-gradient(135deg,#4a3a28,#1c1610)}
.promo-new .t1{position:absolute;left:92px;top:62px;font-weight:800;font-size:30px;color:var(--orange)}
.btn-small{position:absolute;background:var(--orange);color:var(--white);font-weight:700;font-size:13px;text-align:center}
.promo-friday{left:617px;top:1210px;width:481px;height:499px;background:linear-gradient(135deg,#2a2a2a,#0e0e0e)}
.promo-friday .frame{position:absolute;left:60px;top:50px;width:362px;height:388px;border:16px solid var(--orange)}
.promo-friday .t1{position:absolute;top:96px;width:100%;text-align:center;font-weight:800;font-size:30px}
.promo-friday .t2{position:absolute;top:160px;width:100%;text-align:center;font-weight:800;font-size:58px;line-height:62px;color:var(--orange)}

/* section titles */
.kicker{left:0;width:1200px;text-align:center;font-size:19px;color:var(--ink)}
.section-title{left:0;width:1200px;text-align:center;font-family:'Montserrat',sans-serif;font-weight:900;font-size:50px;color:var(--ink)}
.section-title::before,.section-title::after{content:"";display:inline-block;width:10px;height:10px;background:var(--orange);border-radius:50%;vertical-align:middle;margin:0 26px}

/* products */
.card{width:240px;height:335px;border:1px solid var(--line);background:var(--white)}
.card .ph{position:absolute;left:40px;top:25px;width:160px;height:160px;border-radius:6px}
.card .badge{position:absolute;right:0;top:14px;width:50px;height:24px;font-size:12px;font-weight:700;color:var(--white);text-align:center;line-height:24px;background:var(--orange)}
.card .badge.sale{background:var(--red)}
.card .name{position:absolute;top:232px;width:100%;text-align:center;font-size:14px;color:var(--ink);text-transform:uppercase}
.card .stars{position:absolute;top:256px;width:100%;text-align:center;font-size:15px;color:var(--orange);letter-spacing:1px}
.card .price{position:absolute;top:280px;width:100%;text-align:center;font-family:'Montserrat',sans-serif;font-weight:700;font-size:22px;color:var(--ink)}
.card .price s{font-weight:400;font-size:18px;color:var(--muted);margin-left:6px}
.round-arrow{width:38px;height:38px;border-radius:50%;border:1px solid #ccc;background:var(--white);display:flex;align-items:center;justify-content:center}

/* flat banner */
.flat-banner{left:104px;top:2434px;width:994px;height:248px;background:linear-gradient(90deg,#4d4842 0%,#6f6359 45%,#8b3b33 75%,#b3261e 100%)}
.flat-banner h2{position:absolute;left:60px;top:60px;width:500px;text-align:center;font-family:'Montserrat',sans-serif;font-weight:900;font-size:44px;line-height:60px;color:var(--white)}

/* tabs */
.tab{top:2923px;height:42px;border:1px solid #ccc;font-family:'Montserrat',sans-serif;font-weight:600;font-size:13px;line-height:40px;text-align:center;color:var(--ink)}
.tab.on{background:var(--orange);border-color:var(--orange);color:var(--white)}
.view-more{left:514px;top:3472px;width:172px;height:57px;background:var(--orange);color:var(--white);font-family:'Montserrat',sans-serif;font-weight:700;font-size:17px;text-align:center;line-height:57px}

/* brands */
.brands{top:3626px;left:0;width:1200px;height:208px;background:var(--band)}
.brand{top:30px;width:178px;height:148px;background:var(--white);display:flex;align-items:center;justify-content:center;font-family:'Montserrat',sans-serif;font-weight:700;font-size:22px;color:var(--ink)}

/* blog */
.post{top:4114px;width:306px}
.post .ph{height:198px}
.post .meta{margin-top:22px;font-size:12px;color:var(--muted)}
.post .meta b{color:var(--orange);font-weight:500}
.post h3{margin-top:10px;font-family:'Montserrat',sans-serif;font-weight:700;font-size:16px;color:var(--ink)}
.post .read{margin-top:22px;width:146px;height:44px;background:#333;color:var(--white);font-family:'Montserrat',sans-serif;font-weight:700;font-size:12px;line-height:44px;text-align:center}

/* newsletter */
.newsletter{top:4538px;left:0;width:1200px;height:86px;background:var(--orange)}
.newsletter p{position:absolute;left:77px;top:31px;font-family:'Montserrat',sans-serif;font-weight:700;font-size:20px;color:var(--white)}
.newsletter .field{position:absolute;left:706px;top:25px;width:272px;height:38px;background:var(--white);font-size:13px;color:var(--muted);padding:11px 16px}
.newsletter .send{position:absolute;left:978px;top:25px;width:102px;height:38px;background:#333;color:var(--white);font-family:'Montserrat',sans-serif;font-weight:700;font-size:15px;line-height:38px;text-align:center}

/* footer */
.footer-logo{left:450px;top:4667px;width:300px;text-align:center}
.footer-about{left:255px;top:4860px;width:690px;text-align:center;font-size:15px;line-height:24px;color:var(--text)}
.social{top:4940px;left:0;width:1200px;display:flex;justify-content:center;gap:21px}
.social span{width:44px;height:44px;background:#333;display:block}
.rule{left:104px;width:994px;height:1px;background:var(--line)}
.footer-nav{top:5130px;left:0;width:1200px;display:flex;justify-content:center;gap:46px;font-family:'Montserrat',sans-serif;font-weight:600;font-size:16px;color:var(--ink)}
.payments{top:5247px;left:0;width:1200px;display:flex;justify-content:center;gap:6px}
.payments span{width:52px;height:38px;border:1px solid var(--line);font-size:11px;font-weight:700;color:var(--ink);text-align:center;line-height:38px}
.copyright{top:5335px;left:0;width:1200px;text-align:center;font-size:14px;color:var(--muted)}
</style>
</head>
<body>

<div class="abs topbar">
  <div class="abs login">&#128100; Login / Register</div>
  <div class="abs lang"><span>ENGLISH &#9662;</span><span>$ US DOLLAR &#9662;</span></div>
</div>

<header class="abs header">
  <div class="abs search">Keyword here...
    <svg width="18" height="18" viewBox="0 0 18 18"><circle cx="7.5" cy="7.5" r="5.5" fill="none" stroke="#1d1d1d" stroke-width="2"/><line x1="11.5" y1="11.5" x2="16" y2="16" stroke="#1d1d1d" stroke-width="2.4"/></svg>
  </div>
  <div class="abs logo"><div class="mark"></div><div class="name">Lunar Gear</div></div>
  <div class="abs header-icon" style="left:972px">
    <svg width="18" height="16" viewBox="0 0 24 22"><path d="M12 21 2.5 11.5a5.5 5.5 0 0 1 9.5-6 5.5 5.5 0 0 1 9.5 6Z" fill="#1d1d1d"/></svg>
  </div>
  <div class="abs header-icon" style="left:1044px">
    <svg width="18" height="16" viewBox="0 0 24 22"><path d="M1 2h4l3 12h12l3-9H7" fill="none" stroke="#1d1d1d" stroke-width="2.4"/><circle cx="9" cy="19" r="2" fill="#1d1d1d"/><circle cx="19" cy="19" r="2" fill="#1d1d1d"/></svg>
  </div>
</header>

<nav class="abs nav"><span class="active">HOME</span><span>PRODUCTS</span><span>BRANDS</span><span>CONTACT US</span></nav>

<section class="abs hero" role="img" aria-label="Front view of a black sports car in the dark with headlights on">
  <h1>SELECT YOUR VEHICAL</h1>
  <div class="abs select" style="left:162px">Select Make</div>
  <div class="abs select" style="left:387px">Select Model</div>
  <div class="abs select" style="left:611px">Select Year</div>
  <div class="abs search-btn">SEARCH</div>
  <div class="abs hero-arrow" style="left:48px"></div>
  <div class="abs hero-arrow" style="left:1118px"></div>
</section>

<div class="abs feature" style="left:72px">
  <div class="icon"><svg width="40" height="30" viewBox="0 0 40 30"><path d="M6 18 10 8h20l4 10v6H6Z" fill="none" stroke="#eaa215" stroke-width="2.4"/><circle cx="12" cy="24" r="3" fill="#eaa215"/><circle cx="28" cy="24" r="3" fill="#eaa215"/></svg></div>
  <h3>WORLD WIDE FREE SHIPPING</h3>
  <p>Sed ut perspiciatis unde omnis iste natus error sit voluptatem accusantium doloremque</p>
</div>
<div class="abs feature" style="left:450px">
  <div class="icon"><svg width="38" height="38" viewBox="0 0 38 38"><path d="M31 14A13 13 0 0 0 7 12M7 24a13 13 0 0 0 24 2" fill="none" stroke="#eaa215" stroke-width="2.4"/><path d="M5 6v7h7M33 32v-7h-7" fill="none" stroke="#eaa215" stroke-width="2.4"/></svg></div>
  <h3>MONEY BACK GUARANTEE</h3>
  <p>Sed ut perspiciatis unde omnis iste natus error sit voluptatem accusantium doloremque</p>
</div>
<div class="abs feature" style="left:828px">
  <div class="icon"><svg width="36" height="38" viewBox="0 0 36 38"><path d="M5 20v-4a13 13 0 0 1 26 0v4" fill="none" stroke="#eaa215" stroke-width="2.4"/><rect x="3" y="18" width="6" height="10" rx="2" fill="#eaa215"/><rect x="27" y="18" width="6" height="10" rx="2" fill="#eaa215"/><path d="M30 28c0 5-5 7-10 7" fill="none" stroke="#eaa215" stroke-width="2"/></svg></div>
  <h3>ONLINE SUPPORT 24/24</h3>
  <p>Sed ut perspiciatis unde omnis iste natus error sit voluptatem accusantium doloremque</p>
</div>

<div class="abs promo promo-year" role="img" aria-label="Close-up of engine parts in dark tones">
  <div class="t1">PARTS OF THE YEAR</div>
  <div class="t2">2018</div>
</div>
<div class="abs promo promo-new" role="img" aria-label="Mechanic working on an engine in warm light">
  <div class="t1">NEW ARRIVALS 2019</div>
  <div class="btn-small" style="left:180px;top:160px;width:134px;height:34px;line-height:34px">SHOP NOW</div>
</div>
<div class="abs promo promo-friday" role="img" aria-label="Stacked car tyres in dark tones">
  <div class="frame"></div>
  <div class="t1">BLACK FRIDAY SALE</div>
  <div class="t2">UPTO<br>50 %<br>OFF</div>
  <div class="btn-small" style="left:173px;top:370px;width:134px;height:34px;line-height:34px;background:#fff;color:#1d1d1d">SHOP NOW</div>
</div>

<div class="abs kicker" style="top:1818px">TOP NEW IN THE WEEK</div>
<h2 class="abs section-title" style="top:1850px">NEW ARRIVALS</h2>

<div class="abs card" style="left:79px;top:1992px">
  <div class="ph" role="img" aria-label="Tube of engine sealant" style="background:linear-gradient(#e8eef8,#b9c7e3)"></div>
  <div class="badge">NEW</div>
  <div class="name">Grip Seal Quik Oil 8 oz.</div><div class="stars">★★★★★</div><div class="price">$9.32</div>
</div>
<div class="abs card" style="left:348px;top:1992px">
  <div class="ph" role="img" aria-label="Bottle of gear oil" style="background:linear-gradient(#d7d7d7,#3a2a22)"></div>
  <div class="badge">NEW</div>
  <div class="name">Heavy Drive 75W-140</div><div class="stars">★★★★★</div><div class="price">$17.84<s>$18.63</s></div>
</div>
<div class="abs card" style="left:621px;top:1992px">
  <div class="ph" role="img" aria-label="Black oil catch can" style="background:linear-gradient(#e6e6e6,#2b2b2b)"></div>
  <div class="badge sale">-20 %</div>
  <div class="name">Trapline 200 Oil Catch Can</div><div class="stars">★★★★★</div><div class="price">$106.21<s>$133.10</s></div>
</div>
<div class="abs card" style="left:894px;top:1992px">
  <div class="ph" role="img" aria-label="Pair of control arms" style="background:linear-gradient(135deg,#f2f2f2,#555)"></div>
  <div class="badge">NEW</div>
  <div class="name">Heavy Duty Control Arms</div><div class="stars">★★★★★</div><div class="price">$82.52<s>$93.17</s></div>
</div>
<div class="abs round-arrow" style="left:56px;top:2106px"><svg width="10" height="12"><path d="M8 1 2 6l6 5" fill="none" stroke="#888" stroke-width="2"/></svg></div>
<div class="abs round-arrow" style="left:1100px;top:2106px"><svg width="10" height="12"><path d="M2 1l6 5-6 5" fill="none" stroke="#888" stroke-width="2"/></svg></div>

<div class="abs flat-banner" role="img" aria-label="Red sports car on a desert road">
  <h2>FLAT 50 % OFF<br>ON SELECTED PRODUCTS</h2>
</div>

<div class="abs kicker" style="top:2791px">TOP SALE IN THE WEEK</div>
<h2 class="abs section-title" style="top:2826px">BEST SELLERS</h2>
<div class="abs tab on" style="left:320px;width:216px">REPLACEMENT PARTS</div>
<div class="abs tab" style="left:553px;width:148px">SMART DEVICES</div>
<div class="abs tab" style="left:716px;width:164px">WHEELS &amp; TIRES</div>

<div class="abs card" style="left:79px;top:3041px">
  <div class="ph" role="img" aria-label="Black oil catch can" style="background:linear-gradient(#e6e6e6,#2b2b2b)"></div>
  <div class="badge">NEW</div>
  <div class="name">Trapline 200 Oil Catch</div><div class="stars">★★★★★</div><div class="price">$106.21<s>$133.10</s></div>
</div>
<div class="abs card" style="left:348px;top:3041px">
  <div class="ph" role="img" aria-label="Bottle of synthetic motor oil" style="background:linear-gradient(#e0e0e0,#8a2a22)"></div>
  <div class="name">Kore 20W50 Synthetic</div><div class="stars">★★★★★</div><div class="price">$14.64</div>
</div>
<div class="abs card" style="left:621px;top:3041px">
  <div class="ph" role="img" aria-label="Sway bar bushings" style="background:linear-gradient(#eaeaf2,#1d2040)"></div>
  <div class="badge sale">-20 %</div>
  <div class="name">Stayflex Sway Bar</div><div class="stars">★★★★★</div><div class="price">$33.28</div>
</div>
<div class="abs card" style="left:894px;top:3041px">
  <div class="ph" role="img" aria-label="Rubber spring seats" style="background:linear-gradient(#eee,#222)"></div>
  <div class="name">Stayflex Spring Seat</div><div class="stars">★★★★★</div><div class="price">$69.21</div>
</div>
<div class="abs round-arrow" style="left:56px;top:3152px"><svg width="10" height="12"><path d="M8 1 2 6l6 5" fill="none" stroke="#888" stroke-width="2"/></svg></div>
<div class="abs round-arrow" style="left:1100px;top:3152px"><svg width="10" height="12"><path d="M2 1l6 5-6 5" fill="none" stroke="#888" stroke-width="2"/></svg></div>

<div class="abs view-more">VIEW MORE</div>

<section class="abs brands">
  <div class="abs brand" style="left:129px">Corsaro</div>
  <div class="abs brand" style="left:383px">Oakfield</div>
  <div class="abs brand" style="left:636px">Kaito</div>
  <div class="abs brand" style="left:888px">Halden</div>
  <div class="abs round-arrow" style="left:110px;top:86px"><svg width="10" height="12"><path d="M8 1 2 6l6 5" fill="none" stroke="#888" stroke-width="2"/></svg></div>
  <div class="abs round-arrow" style="left:1050px;top:86px"><svg width="10" height="12"><path d="M2 1l6 5-6 5" fill="none" stroke="#888" stroke-width="2"/></svg></div>
</section>

<div class="abs kicker" style="top:3926px">OUR RECENT POSTS</div>
<h2 class="abs section-title" style="top:3960px">LATEST BLOGS</h2>

<article class="abs post" style="left:100px">
  <div class="ph" role="img" aria-label="Dark sports car on a road at dusk" style="background:linear-gradient(135deg,#8fa4bd,#1a1e26)"></div>
  <div class="meta">MARCH 6 2019 &nbsp; BY <b>RAMI SALEH</b></div>
  <h3>BITEN DEMONS LECTOR IN HENDER</h3>
  <div class="read">READ MORE</div>
</article>
<article class="abs post" style="left:441px">
  <div class="ph" role="img" aria-label="White SUV parked outdoors" style="background:linear-gradient(135deg,#5a5a5a,#c9c9c9)"></div>
  <div class="meta">MARCH 6 2019 &nbsp; BY <b>RAMI SALEH</b></div>
  <h3>BITEN DEMONS LECTOR IN HENDER</h3>
  <div class="read">READ MORE</div>
</article>
<article class="abs post" style="left:786px">
  <div class="ph" role="img" aria-label="Pile of metal gears and bearings" style="background:linear-gradient(135deg,#b8b8b8,#3c3c3c)"></div>
  <div class="meta">MARCH 6 2019 &nbsp; BY <b>RAMI SALEH</b></div>
  <h3>BITEN DEMONS LECTOR IN HENDER</h3>
  <div class="read">READ MORE</div>
</article>

<section class="abs newsletter">
  <p>SIGN UP FOR NEWSLETTER &amp; GET 20% OFF ON FIRST ORDER</p>
  <div class="field">Enter your email</div>
  <div class="send">SEND</div>
</section>

<footer>
  <div class="abs footer-logo logo" style="top:4667px"><div class="mark"></div><div class="name">Lunar Gear</div></div>
  <p class="abs footer-about">Lorem ipsum dolor sit amet, consectetur adipiscing elit, sed do eiusmod tempor incididunt ut labore et dolore magna aliqua. Quis ipsum suspendisse ultrices gravida. Risus commodo viverra maecenas ac.</p>
  <div class="abs social"><span></span><span></span><span></span><span></span><span></span><span></span></div>
  <div class="abs rule" style="top:5073px"></div>
  <nav class="abs footer-nav"><span>HOME</span><span>PRODUCTS</span><span>BRANDS</span><span>CONTACT US</span></nav>
  <div class="abs rule" style="top:5202px"></div>
  <div class="abs payments"><span>Paylo</span><span>Cardix</span><span>Novapay</span><span>Orbit</span></div>
  <div class="abs copyright">Lunar Gear © 2016. All Rights Reserved.</div>
</footer>

</body>
</html>
```